Renewal of the Ferravolt SA Website

Ferravolt SA is a metal construction company active in industrial piping, boilermaking and metal framing. We would like to renew our site.

This website must be ready to work with Wordpress.

The site will contain the following pages: Home, skills, presentation, contact.

The site must reflect the field of the metal construction sector. It must be clear and easily understandable. The objective is not to win mandates with but to present the company and its capabilities.

I have inserted the pages of our old presentations, to describe our sector but we do not want to reuse these elements, we are waiting for your creativity to surprise us. In the 2nd phase we will complete with new images if necessary and texts

Target Market(s)

International companies in the food, chemical and pharmaceutical sectors

Industry/Entity Type

Alimentaire, pharma, chimie

Number of Pages Required

4 page

Font styles to use
Sans Serif

Colors
0054AA
0677BA
7BADD7
CADEEF
E8F1F8

Requirements
Must have
• It must contain at least the requested pages, images of illustrations, places for descriptions
Should not have
• Elements that appear or disappear, too flash,

```html
<!DOCTYPE html>
<html lang="en">
<head>
<meta charset="utf-8">
<title>Ferravolt SA — Metal Construction</title>
<link rel="stylesheet" href="https://fonts.googleapis.com/css2?family=Lato:wght@400;700;900&display=swap">
<style>
:root{
  --blue:#1d47a6;
  --navy:#1a3a7a;
  --deep:#0f2f6e;
  --ink:#111;
  --grey:#8a8b90;
  --muted:#6a6a6a;
  --white:#fff;
  --black:#000;
}
*{box-sizing:border-box;margin:0;padding:0}
html,body{width:1200px;height:2955px;overflow:hidden;background:#fff}
body{font-family:'Lato',sans-serif;color:var(--ink)}
.page{position:relative;width:1200px;height:2955px;overflow:hidden}
.abs{position:absolute}
/* header */
.topbar{left:551px;top:0;width:649px;height:49px;background:var(--blue);clip-path:polygon(0 0,100% 0,100% 100%,40px 100%);color:#fff;font-size:16px;display:flex;align-items:center;gap:14px;padding-left:48px}
.topbar svg{flex:none}
.topbar .sep{opacity:.6;margin:0 6px}
.brand{left:109px;top:42px;font-size:38px;font-weight:900;color:var(--navy);letter-spacing:1px;display:flex;align-items:center;gap:12px}
.brand .dot{width:26px;height:26px;border-radius:50%;background:var(--navy)}
.nav{top:80px;font-size:16px;letter-spacing:.3px;color:#222}
.nav.active{color:var(--blue);font-weight:700;border-bottom:2px solid var(--blue)}
/* hero */
.hero{left:0;top:126px;width:1200px;height:680px}
.hero-text{left:112px;top:256px;color:#fff}
.hero-text .welcome{font-size:22px;letter-spacing:.5px}
.hero-text h1{font-size:68px;font-weight:900;letter-spacing:1px;margin-top:10px;line-height:1}
.hero-text p{font-size:15px;font-weight:700;line-height:26px;width:380px;margin-top:18px}
.btn-light{display:inline-block;margin-top:26px;background:#fff;color:var(--blue);font-weight:700;font-size:19px;padding:13px 18px;border-radius:6px}
/* section titles */
.title{width:1200px;text-align:center;font-size:35px;font-weight:900;letter-spacing:.5px}
.title span{color:var(--navy)}
/* services */
.svc{width:296px}
.svc .photo{height:252px;width:296px}
.svc .cap{position:absolute;left:32px;top:236px;width:264px;background:#fff;text-align:center;padding-top:12px}
.svc h3{font-size:18px;font-weight:700;letter-spacing:.3px}
.svc p{font-size:11px;line-height:20px;margin-top:6px;padding:0 26px}
.arrow{width:34px;height:34px;border-radius:50%;background:#000;display:flex;align-items:center;justify-content:center}
/* about */
.about-text{left:661px;top:1392px;width:427px;color:#fff}
.about-text h2{font-size:36px;font-weight:900;letter-spacing:.6px}
.about-text p{font-size:17px;line-height:29px;text-align:justify;margin-top:16px}
.about-text p+p{margin-top:29px}
.btn-blue{display:inline-block;margin-top:30px;background:var(--blue);color:#fff;font-weight:700;font-size:19px;padding:13px 24px;border-radius:6px;box-shadow:0 4px 8px rgba(0,0,0,.25)}
/* testimonials */
.tcard{width:300px;height:195px;background:#fff;border-radius:6px;box-shadow:0 2px 14px rgba(0,0,0,.09);text-align:center;padding-top:52px}
.tcard h4{font-size:18px;font-weight:700;color:#333}
.tcard .stars{color:#f3b43c;font-size:12px;letter-spacing:1px;margin-top:4px}
.tcard p{font-size:13px;line-height:26px;color:var(--muted);margin-top:6px;padding:0 18px}
.tcard.featured h4,.tcard.featured p{color:#111}
.avatar{width:72px;height:72px;border-radius:50%;border:4px solid #fff;box-shadow:0 1px 6px rgba(0,0,0,.15);background:linear-gradient(#c8cdd3,#9aa3ad)}
/* footer */
.field{height:51px;border:1px solid #555;border-radius:3px;color:#fff;font-size:13px;font-weight:700;padding:17px 16px;background:#000}
.subscribe{height:51px;width:172px;background:var(--blue);color:#fff;font-weight:900;font-size:14px;letter-spacing:.5px;border-radius:3px;display:flex;align-items:center;justify-content:center}
.rule{left:110px;width:978px;height:1px;background:#555}
.flogo{left:111px;top:2615px;width:260px;height:99px;background:#fff;display:flex;align-items:center;justify-content:center;gap:10px;font-size:30px;font-weight:900;color:var(--navy)}
.flogo .dot{width:22px;height:22px;border-radius:50%;background:var(--navy)}
.fcol{color:#fff}
.fcol h5{font-size:18px;font-weight:400;letter-spacing:.4px;margin-bottom:6px}
.fcol li{list-style:none;font-size:15px;height:34.4px;display:flex;align-items:center;gap:14px}
.citem{display:flex;gap:14px;align-items:flex-start;font-size:15px;line-height:27px;color:#fff}
.ico{width:28px;height:28px;border-radius:50%;border:1.5px solid #fff;display:flex;align-items:center;justify-content:center;flex:none}
.copy{left:110px;top:2904px;color:#fff;font-size:13px}
.social{width:28px;height:28px;border-radius:50%;border:1.5px solid #fff}
</style>
</head>
<body>
<div class="page">

<!-- header -->
<div class="abs topbar">
  <svg width="18" height="18" viewBox="0 0 24 24" fill="#fff"><path d="M6.6 10.8a15 15 0 0 0 6.6 6.6l2.2-2.2c.3-.3.7-.4 1-.2 1.1.4 2.3.6 3.6.6.6 0 1 .4 1 1V20c0 .6-.4 1-1 1A17 17 0 0 1 3 4c0-.6.4-1 1-1h3.5c.6 0 1 .4 1 1 0 1.3.2 2.5.6 3.6.1.3 0 .7-.2 1z"/></svg>
  <span class="sep">|</span><span>Call:+1 555 014 2290</span>
  <svg style="margin-left:18px" width="18" height="14" viewBox="0 0 24 18" fill="#fff"><path d="M0 0h24v18H0z"/><path d="M0 0l12 9 12-9" stroke="#1d47a6" stroke-width="2" fill="none"/></svg>
  <span class="sep">|</span><span>Mail:info@ferravolt.com</span>
</div>
<div class="abs brand"><span class="dot"></span>FERRAVOLT</div>
<div class="abs nav active" style="left:528px">HOME</div>
<div class="abs nav" style="left:623px">ABOUT</div>
<div class="abs nav" style="left:723px">SERVICES</div>
<div class="abs nav" style="left:837px">TESTIMONIALS</div>
<div class="abs nav" style="left:992px">CONTACT US</div>

<!-- hero -->
<svg class="abs hero" viewBox="0 0 1200 680" role="img" aria-label="Warehouse interior with rows of rolled steel coils">
  <defs>
    <linearGradient id="heroFill" x1="0" y1="0" x2="1" y2="1">
      <stop offset="0" stop-color="#1c2430"/>
      <stop offset=".45" stop-color="#3b4654"/>
      <stop offset=".75" stop-color="#5a5650"/>
      <stop offset="1" stop-color="#1e2228"/>
    </linearGradient>
  </defs>
  <polygon points="0,0 1200,0 1200,654 0,551" fill="url(#heroFill)"/>
  <polygon points="430,595 1200,654 1200,680 700,630" fill="#1d47a6"/>
  <polygon points="380,590 1200,660 1200,664 700,622" fill="#0f2f6e"/>
</svg>
<div class="abs hero-text">
  <div class="welcome">WELCOME TO</div>
  <h1>FERRAVOLT</h1>
  <p>Itaque earum rerum hic tenetur a sapiente delectus, ut aut reiciendis voluptatibus maiores alias consequatur aut perferendis doloribus asperiores repellat.</p>
  <span class="btn-light">GET STARTED</span>
</div>

<!-- services -->
<div class="abs title" style="left:0;top:823px">OUR <span>SERVICES</span></div>
<div class="abs arrow" style="left:35px;top:1057px"><svg width="12" height="14" viewBox="0 0 12 14"><path d="M9 1 3 7l6 6" stroke="#fff" stroke-width="3" fill="none"/></svg></div>
<div class="abs arrow" style="left:1123px;top:1057px"><svg width="12" height="14" viewBox="0 0 12 14"><path d="M3 1l6 6-6 6" stroke="#fff" stroke-width="3" fill="none"/></svg></div>

<div class="abs svc" style="left:111px;top:903px">
  <div class="photo" role="img" aria-label="Industrial piping installation at a plant" style="background:linear-gradient(160deg,#b9c1c8,#8f3a32 55%,#5c646c)"></div>
  <div class="cap"><h3>INDUSTRIAL PIPING</h3><p>Temporibus autem quibusdam et aut officiis debitis aut rerum</p></div>
</div>
<div class="abs svc" style="left:452px;top:903px">
  <div class="photo" role="img" aria-label="Welder working with sparks in boilermaking" style="background:linear-gradient(150deg,#1c3f74,#6a3a1c 55%,#e89a3a)"></div>
  <div class="cap"><h3>BOILERMAKING</h3><p>Temporibus autem quibusdam et aut officiis debitis aut rerum</p></div>
</div>
<div class="abs svc" style="left:791px;top:903px">
  <div class="photo" role="img" aria-label="Steel stud metal framing structure" style="background:linear-gradient(90deg,#6f7a86,#c9d0d6 50%,#7c8590)"></div>
  <div class="cap"><h3>METAL FRAMING</h3><p>Temporibus autem quibusdam et aut officiis debitis aut rerum</p></div>
</div>

<!-- about -->
<svg class="abs" style="left:0;top:1270px" width="1200" height="640" viewBox="0 0 1200 640" role="img" aria-label="Worker in hard hat cutting metal with an angle grinder">
  <defs>
    <linearGradient id="aboutFill" x1="0" y1="0" x2="1" y2="0">
      <stop offset="0" stop-color="#2a2a2e"/>
      <stop offset=".3" stop-color="#4a3a30"/>
      <stop offset=".55" stop-color="#8a8b90"/>
      <stop offset="1" stop-color="#8a8b90"/>
    </linearGradient>
  </defs>
  <polygon points="0,106 1200,26 1200,604 0,506" fill="url(#aboutFill)"/>
  <polygon points="470,72 1200,0 1200,26 700,56" fill="#1d47a6"/>
  <polygon points="440,74 1200,20 1200,24 700,52" fill="#0f2f6e"/>
  <polygon points="230,516 1200,604 1200,636 700,570" fill="#0f2f6e"/>
  <polygon points="260,518 1200,590 1200,602 700,556" fill="#1d47a6"/>
</svg>
<div class="abs about-text">
  <h2>ABOUT FERRAVOLT</h2>
  <p>Nam libero tempore, cum soluta nobis est eligendi optio cumque nihil impedit quo minus id quod maxime placeat facere possimus, omnis voluptas assumenda est, omnis dolor repellendus.</p>
  <p>Temporibus autem quibusdam et aut officiis debitis aut rerum necessitatibus saepe eveniet ut et voluptates repudiandae sint et molestiae non recusandae.</p>
  <span class="btn-blue">READ MORE</span>
</div>

<!-- testimonials -->
<div class="abs title" style="left:0;top:1924px">WHAT <span>CUSTOMER SAYS</span></div>
<div class="abs tcard" style="left:109px;top:2042px"><h4>Marcus Ellery</h4><div class="stars">★★★★★</div><p>Temporibus autem quibusdam et aut officiis debitis aut rerum necessitatibus saepe eveniet ut et voluptates</p></div>
<div class="abs tcard featured" style="left:448px;top:2042px"><h4>Julian Brandt</h4><div class="stars">★★★★★</div><p>Itaque earum rerum hic tenetur a sapiente delectus, reiciendis voluptatibus maiores alias consequatur aut</p></div>
<div class="abs tcard" style="left:787px;top:2042px"><h4>Clara Winsome</h4><div class="stars">★★★★★</div><p>Nam libero tempore, cum soluta nobis est eligendi optio cumque nihil impedit quo minus id quod</p></div>
<div class="abs avatar" role="img" aria-label="Customer portrait" style="left:223px;top:2008px"></div>
<div class="abs avatar" role="img" aria-label="Customer portrait" style="left:562px;top:2008px"></div>
<div class="abs avatar" role="img" aria-label="Customer portrait" style="left:901px;top:2008px"></div>

<!-- footer -->
<svg class="abs" style="left:0;top:2270px" width="1200" height="685" viewBox="0 0 1200 685">
  <polygon points="0,8 1200,133 1200,685 0,685" fill="#000"/>
  <polygon points="0,0 820,90 1200,133 0,22" fill="#000"/>
  <polygon points="0,0 820,92 0,14" fill="#1d47a6"/>
  <polygon points="0,14 820,92 0,22" fill="#fff"/>
</svg>

<div class="abs field" style="left:110px;top:2468px;width:181px">First Name:</div>
<div class="abs field" style="left:311px;top:2468px;width:180px">Email:</div>
<div class="abs field" style="left:510px;top:2468px;width:181px">Phone:</div>
<div class="abs field" style="left:712px;top:2468px;width:181px">Address:</div>
<div class="abs subscribe" style="left:914px;top:2468px">SUBSCRIBE</div>
<div class="abs rule" style="top:2562px"></div>

<div class="abs flogo"><span class="dot"></span>FERRAVOLT</div>

<div class="abs fcol" style="left:438px;top:2616px">
  <h5>QUICK LINKS</h5>
  <ul>
    <li><svg width="20" height="12" viewBox="0 0 20 12"><path d="M0 6h18M12 1l6 5-6 5" stroke="#fff" stroke-width="2" fill="none"/></svg>Home</li>
    <li><svg width="20" height="12" viewBox="0 0 20 12"><path d="M0 6h18M12 1l6 5-6 5" stroke="#fff" stroke-width="2" fill="none"/></svg>About</li>
    <li><svg width="20" height="12" viewBox="0 0 20 12"><path d="M0 6h18M12 1l6 5-6 5" stroke="#fff" stroke-width="2" fill="none"/></svg>Services</li>
    <li><svg width="20" height="12" viewBox="0 0 20 12"><path d="M0 6h18M12 1l6 5-6 5" stroke="#fff" stroke-width="2" fill="none"/></svg>Why Choose Us</li>
    <li><svg width="20" height="12" viewBox="0 0 20 12"><path d="M0 6h18M12 1l6 5-6 5" stroke="#fff" stroke-width="2" fill="none"/></svg>Contact Us</li>
  </ul>
</div>
<div class="abs fcol" style="left:666px;top:2616px">
  <h5>HELP LINKS</h5>
  <ul>
    <li><svg width="20" height="12" viewBox="0 0 20 12"><path d="M0 6h18M12 1l6 5-6 5" stroke="#fff" stroke-width="2" fill="none"/></svg>FAQ</li>
    <li><svg width="20" height="12" viewBox="0 0 20 12"><path d="M0 6h18M12 1l6 5-6 5" stroke="#fff" stroke-width="2" fill="none"/></svg>Support Links</li>
    <li><svg width="20" height="12" viewBox="0 0 20 12"><path d="M0 6h18M12 1l6 5-6 5" stroke="#fff" stroke-width="2" fill="none"/></svg>Privacy Policy</li>
    <li><svg width="20" height="12" viewBox="0 0 20 12"><path d="M0 6h18M12 1l6 5-6 5" stroke="#fff" stroke-width="2" fill="none"/></svg>Term of use</li>
    <li><svg width="20" height="12" viewBox="0 0 20 12"><path d="M0 6h18M12 1l6 5-6 5" stroke="#fff" stroke-width="2" fill="none"/></svg>Terms &amp; Conditions</li>
  </ul>
</div>
<div class="abs fcol" style="left:886px;top:2616px">
  <h5>CONTACT US</h5>
</div>
<div class="abs citem" style="left:884px;top:2650px">
  <span class="ico"><svg width="12" height="15" viewBox="0 0 12 15"><path d="M6 14S1 8.5 1 5.5a5 5 0 0 1 10 0C11 8.5 6 14 6 14z" stroke="#fff" stroke-width="1.6" fill="none"/><circle cx="6" cy="5.5" r="1.8" fill="#fff"/></svg></span>
  <span>Ferravolt<br>United States</span>
</div>
<div class="abs citem" style="left:884px;top:2714px">
  <span class="ico"><svg width="12" height="9" viewBox="0 0 12 9"><rect width="12" height="9" fill="#fff"/><path d="M0 0l6 5 6-5" stroke="#000" stroke-width="1.2" fill="none"/></svg></span>
  <span>info@ferravolt.com</span>
</div>
<div class="abs citem" style="left:884px;top:2766px">
  <span class="ico"><svg width="13" height="13" viewBox="0 0 24 24" fill="#fff"><path d="M6.6 10.8a15 15 0 0 0 6.6 6.6l2.2-2.2c.3-.3.7-.4 1-.2 1.1.4 2.3.6 3.6.6.6 0 1 .4 1 1V20c0 .6-.4 1-1 1A17 17 0 0 1 3 4c0-.6.4-1 1-1h3.5c.6 0 1 .4 1 1 0 1.3.2 2.5.6 3.6.1.3 0 .7-.2 1z"/></svg></span>
  <span>+1 555 014 2290</span>
</div>

<div class="abs rule" style="top:2872px"></div>
<div class="abs copy">Copyrights@2023.Ferravolt.All Rights Reserved</div>
<div class="abs social" style="left:965px;top:2902px"></div>
<div class="abs social" style="left:1016px;top:2902px"></div>
<div class="abs social" style="left:1061px;top:2902px"></div>

</div>
</body>
</html>
```